Machine shop needs a brochure designed

Would like a tri-fold professional looking brochure that tells about our business and our capabilities. We are a family-owned business with over 50 years of experience in precision manufacturing. We specialize in close-tolerance tooling and serve a diverse array of industries. Our colors are red, black, white, and gray. The final design should make a great impression and spotlight our capabilities and quality.

Target Market(s)

Manufacturing industries needing tooling

Industry/Entity Type

Machining, grinding, manufacturing

Font styles to use
Serif

Colors
EB3D1F
EC4F4E
F09395
F8D3D4
FCEDEE

Requirements
Must have
• Logo, colors are red, black, white, gray
Nice to have
• Images of CNC process or machining/grinding metal parts.

```html
<!DOCTYPE html>
<html lang="en">
<head>
<meta charset="utf-8">
<title>Torvane Industries Tri-fold Brochure</title>
<link href="https://fonts.googleapis.com/css2?family=Bebas+Neue&family=Poppins:wght@400;500;600;700&display=swap" rel="stylesheet">
<style>
:root{
  --red:#e8212a;
  --red-dark:#c41a1f;
  --navy:#2a2d3e;
  --ink:#23263a;
  --text:#2b2b2b;
  --paper:#ffffff;
  --bg:#e7e8ea;
  --soft-gray:#e9eaee;
}
*{box-sizing:border-box;margin:0;padding:0}
html,body{width:849px;height:1200px;overflow:hidden}
body{background:var(--bg);font-family:"Poppins",sans-serif;color:var(--text);position:relative}
.spread{position:absolute;left:107px;width:635px;height:454px;display:flex;background:var(--paper);overflow:hidden}
.spread--outside{top:86px}
.spread--inside{top:648px}
.panel{position:relative;height:100%;flex:none}
.heading{font-family:"Bebas Neue",sans-serif;font-weight:400;line-height:.95;letter-spacing:.2px}
.body-copy{font-size:7.6px;line-height:12.5px}
.photo-frame{position:absolute}
.photo-frame svg.frame{position:absolute;inset:0;width:100%;height:100%}
.photo{position:absolute;border-radius:14px}
.brand{font-family:"Poppins",sans-serif;font-weight:600;display:flex;align-items:center;justify-content:center;gap:5px}
.brand-mark{display:inline-block;width:9px;height:9px}

/* outside */
.panel--mission{width:210px}
.panel--mission .company-title{position:absolute;left:21px;top:32px;font-size:22px;color:var(--ink)}
.panel--mission .body-copy{position:absolute;left:22px;top:328px;width:175px}
.panel--contact{width:210px;background:linear-gradient(160deg,#d92026,#e8262b 50%,#c91d22)}
.panel--contact .brand{position:absolute;left:67px;top:35px;width:83px;height:48px;border:2px solid #fff;color:#fff;font-size:12px;background:var(--red)}
.panel--contact .brand-mark{background:#fff}
.contact-card{position:absolute;left:17px;top:114px;width:178px;height:311px}
.contact-card svg{position:absolute;inset:0}
.contact-card .heading{position:absolute;top:20px;width:100%;text-align:center;color:#fff;font-size:28px}
.contact-list{position:absolute;top:56px;width:100%;list-style:none;text-align:center;color:#fff;font-size:10px}
.contact-list li{height:45.5px;display:flex;flex-direction:column;align-items:center;gap:3px}
.contact-list li.address{line-height:12px}
.contact-list svg{width:22px;height:22px;position:static}
.panel--welcome{width:215px;background:linear-gradient(90deg,#d8d9dc,#f4f4f5 12%,#fff 30%)}
.panel--welcome .brand{position:absolute;left:75px;top:22px;width:58px;height:33px;color:var(--red);font-size:11px}
.panel--welcome .brand-mark{background:var(--red)}
.welcome-title{position:absolute;left:0;width:100%;text-align:center}
.welcome-title .line1{display:block;font-size:42px;color:var(--ink);margin-top:329px}
.welcome-title .line2{display:block;font-size:42px;color:var(--red);margin-top:-2px}
.welcome-title .tag{display:inline-block;background:var(--ink);color:#fff;font-size:10px;font-weight:500;padding:1px 6px;margin-top:2px}

/* inside */
.panel--intro{width:214px}
.panel--intro .heading{position:absolute;left:22px;top:278px}
.panel--intro .heading .dark{display:block;font-size:24px;color:var(--ink)}
.panel--intro .heading .accent{display:block;font-size:19px;color:var(--red)}
.panel--intro .body-copy{position:absolute;left:22px;top:325px;width:176px}
.panel--about{width:207px;background:linear-gradient(180deg,#343748,#2c2f40);color:#e6e7ec}
.panel--about .heading{position:absolute;left:16px;top:22px;font-size:19px;color:var(--red)}
.about-copy{position:absolute;left:16px;top:45px;width:180px;font-size:7.6px;line-height:11.5px}
.about-copy p{margin-bottom:11.5px}
.about-copy strong{font-weight:600;color:#fff}
.signoff{color:var(--red);font-weight:700;display:flex;justify-content:space-between}
.signoff .right{text-align:right;align-self:flex-end}
.panel--capabilities{width:214px;background:linear-gradient(90deg,#dcdde0,#f6f6f7 10%,#fff 28%)}
.panel--capabilities .intro{position:absolute;left:16px;top:20px;width:180px;font-size:7.6px;line-height:11.5px}
.cap-label{position:absolute;left:14px;top:46px;width:138px;height:16px;background:var(--red);color:#fff;font-size:8px;font-weight:700;padding:2px 5px;border-radius:6px 0 0 0}
.cap-list{position:absolute;left:16px;top:68px;width:186px;list-style:none;font-size:7.6px;line-height:11px;display:grid;grid-template-columns:101px 85px}
.cap-list li{position:relative;padding-left:7px}
.cap-list li::before{content:"";position:absolute;left:0;top:4px;width:3px;height:3px;border-radius:50%;background:var(--red)}
.cap-list li.wide{grid-column:1 / span 2}
</style>
</head>
<body>

<!-- Outside spread -->
<section class="spread spread--outside">
  <div class="panel panel--mission">
    <h1 class="heading company-title">Torvane Industries, Inc.</h1>
    <div class="photo-frame" style="left:22px;top:65px;width:175px;height:253px">
      <svg class="frame" viewBox="0 0 175 253" preserveAspectRatio="none">
        <path d="M80 10 L160 0 Q175 0 175 14 L175 40 Q170 18 150 16 Z" fill="var(--navy)"/>
        <path d="M0 220 Q0 248 20 250 L90 240 L20 232 Q4 230 4 215 Z" fill="var(--navy)"/>
      </svg>
      <div class="photo" role="img" aria-label="Photo of a worker grinding metal with an angle grinder, sparks flying" style="left:6px;top:11px;width:162px;height:233px;background:linear-gradient(160deg,#4d8fc4,#3a3fb0 45%,#2b2a8a 70%,#d88a2a)"></div>
    </div>
    <p class="body-copy">is committed to quality and consistency. We are constantly striving to implement new ways to adhere to a high mark while providing our clients with their orders in as short a time frame as possible. It is not only our goal, but we understand it to be our responsibility to provide our clients with the highest quality products.</p>
  </div>

  <div class="panel panel--contact">
    <div class="brand"><span class="brand-mark"></span>Torvane</div>
    <div class="contact-card">
      <svg viewBox="0 0 178 311" preserveAspectRatio="none">
        <path d="M20 1 L150 8 Q177 10 177 36 L177 285 Q177 310 152 310 L30 300 Q1 298 1 272 L1 28 Q1 0 20 1 Z" fill="none" stroke="#fff" stroke-width="1"/>
        <path d="M110 6 L155 9 Q177 12 177 36 L177 50 Q172 20 145 18 Z" fill="#fff"/>
        <path d="M1 255 L1 272 Q1 296 30 300 L80 305 L25 285 Q6 278 1 255 Z" fill="#fff"/>
      </svg>
      <h2 class="heading">Contact Us</h2>
      <ul class="contact-list">
        <li><svg viewBox="0 0 24 24"><circle cx="12" cy="12" r="11" fill="none" stroke="#fff" stroke-width="1.3"/><path d="M8.5 7 L10.5 9.5 L9.5 11 Q11 14 13.5 15 L15 14 L17.5 16 Q16.5 18 14.5 17.8 Q9 16.5 7 10 Q7 8 8.5 7 Z" fill="#fff"/></svg>555.204.7180</li>
        <li><svg viewBox="0 0 24 24"><circle cx="12" cy="12" r="11" fill="none" stroke="#fff" stroke-width="1.3"/><rect x="8.5" y="6.5" width="7" height="3.5" fill="#fff"/><rect x="6.5" y="10" width="11" height="5" rx="1" fill="#fff"/><rect x="8.5" y="13.5" width="7" height="4" fill="#fff" stroke="#e8262b" stroke-width=".8"/></svg>555.204.7181</li>
        <li><svg viewBox="0 0 24 24"><circle cx="12" cy="12" r="11" fill="none" stroke="#fff" stroke-width="1.3"/><rect x="6.5" y="8" width="11" height="8" fill="#fff"/><path d="M6.5 8 L12 12.5 L17.5 8" fill="none" stroke="#e8262b" stroke-width=".9"/></svg>info@torvaneworks.example</li>
        <li><svg viewBox="0 0 24 24"><circle cx="12" cy="12" r="11" fill="none" stroke="#fff" stroke-width="1.3"/><circle cx="12" cy="12" r="6" fill="none" stroke="#fff" stroke-width="1"/><ellipse cx="12" cy="12" rx="2.6" ry="6" fill="none" stroke="#fff" stroke-width="1"/><path d="M6 12 H18 M7 9 H17 M7 15 H17" stroke="#fff" stroke-width=".8"/></svg>www.torvaneworks.example</li>
        <li class="address"><svg viewBox="0 0 24 24"><circle cx="12" cy="12" r="11" fill="none" stroke="#fff" stroke-width="1.3"/><path d="M12 18 Q7.5 12.5 7.5 10 A4.5 4.5 0 0 1 16.5 10 Q16.5 12.5 12 18 Z" fill="#fff"/><circle cx="12" cy="10" r="1.6" fill="#e8262b"/></svg>1480 Harlow Mill Road<br>Westbrook, TN 37000</li>
      </ul>
    </div>
  </div>

  <div class="panel panel--welcome">
    <div class="brand"><span class="brand-mark"></span>Torvane</div>
    <div class="photo-frame" style="left:16px;top:61px;width:179px;height:264px">
      <svg class="frame" viewBox="0 0 179 264" preserveAspectRatio="none">
        <path d="M0 45 L0 20 Q0 0 20 0 L116 9 L30 16 Q4 20 0 45 Z" fill="var(--navy)"/>
        <path d="M179 210 L179 238 Q179 262 155 262 L80 250 L150 246 Q176 242 179 210 Z" fill="var(--navy)"/>
      </svg>
      <div class="photo" role="img" aria-label="Photo of a CNC milling spindle cutting a metal block, blue tones" style="left:5px;top:11px;width:168px;height:242px;background:linear-gradient(160deg,#3c6f95,#1e3f5c 45%,#0f2438 80%,#2c4a66)"></div>
    </div>
    <h2 class="heading welcome-title"><span class="line1">Welcome</span><span class="line2">To Torvane</span><span class="tag">INDUSTRIES, INC.</span></h2>
  </div>
</section>

<!-- Inside spread -->
<section class="spread spread--inside">
  <div class="panel panel--intro">
    <div class="photo-frame" style="left:22px;top:22px;width:176px;height:240px">
      <svg class="frame" viewBox="0 0 176 240" preserveAspectRatio="none">
        <path d="M62 10 L150 0 Q176 0 176 24 L176 40 Q172 20 150 18 Z" fill="var(--red)"/>
        <path d="M0 200 L0 220 Q0 240 22 240 L92 232 L26 224 Q3 222 0 200 Z" fill="var(--red)"/>
      </svg>
      <div class="photo" role="img" aria-label="Photo of a laser cutting head slicing a metal sheet with sparks" style="left:6px;top:12px;width:165px;height:224px;background:linear-gradient(165deg,#9fb3bd,#5f7a86 40%,#3b4f58 65%,#c7a25e 80%,#34424a)"></div>
    </div>
    <h2 class="heading"><span class="dark">Welcome To</span><span class="accent">Torvane Industries, Inc.</span></h2>
    <p class="body-copy">When your project or process requires precise, high-quality parts or components, look no further than Torvane. We welcome the opportunity to quote your project, and with 40 years combined experience in precision manufacturing, you can rest assured that jobs placed with us will be done to your satisfaction, every time.</p>
  </div>

  <div class="panel panel--about">
    <h2 class="heading">About Us...</h2>
    <div class="about-copy">
      <p>Torvane Industries, Inc. is a privately owned company with over fifty years of experience in precision manufacturing. Products manufactured include components for a defense missile system during the Gulf War, machine gun barrels, close tolerance can tooling, conveyor slats and rollers, molds, various production tooling for several national industries, pump housings for the gasoline industry, aviation and automotive manufacturing, and various precision machining and grinding jobs.</p>
      <p>Currently, Torvane Industries, Inc. is working with a group of physicians to develop and patent various surgical devices for use in Orthopedic and General Vascular surgeries.</p>
      <p><strong>We at Torvane Industries,</strong> Inc. look forward to the opportunity to work with you and quote any projects you might want us to look at. We take a "Quality first" approach to all of our jobs and we have the determination to get the job done according to our clients' timelines. We are always looking for opportunities to form new alliances and friendships with prospective clients.</p>
      <div class="signoff" style="margin-bottom:11.5px">
        <span>Best regards,<br>Daniel R. Whitford<br>President / Shop Manager</span>
        <span class="right">Mark Whitford<br>COO</span>
      </div>
      <p>Contact us today and let us help you make your product a success!</p>
    </div>
  </div>

  <div class="panel panel--capabilities">
    <p class="intro">We at Torvane offer a wide variety of services to meet your machining and tooling needs.</p>
    <div class="cap-label">OUR CAPABILITIES INCLUDE -</div>
    <ul class="cap-list">
      <li>Soft cutting</li><li>Hard cutting</li>
      <li>CNC Machining</li><li>CNC Milling</li>
      <li>0-2 Micro-finishing</li><li>Light fabrication</li>
      <li class="wide">NAICS 332813, 332721 &amp; 333512</li>
      <li class="wide">Grinding- O.D./ I.D. and Surface/Rotary (Carbide, Steel, etc.)</li>
      <li class="wide">Conveyor assemblies - slats, rollers, etc.</li>
      <li class="wide">Can tooling- Trimmer Knives, Knockouts, Punch Bolts, Printer Mandrels, Cut Edges, Blank and Draw Dies, etc.</li>
      <li class="wide">Wide range of Aerospace and Automotive tooling</li>
    </ul>
    <div class="photo-frame" style="left:16px;top:196px;width:180px;height:236px">
      <svg class="frame" viewBox="0 0 180 236" preserveAspectRatio="none">
        <path d="M60 10 L160 0 Q180 0 180 22 L180 38 Q176 18 154 16 Z" fill="var(--red)"/>
        <path d="M0 190 L0 212 Q0 236 24 234 L90 226 L26 218 Q3 214 0 190 Z" fill="var(--red)"/>
      </svg>
      <div class="photo" role="img" aria-label="Photo of a precision-machined aluminium block part" style="left:6px;top:12px;width:165px;height:216px;background:linear-gradient(150deg,#f2f3f5,#d4d7dc 45%,#a9adb4 75%,#7e838b)"></div>
    </div>
  </div>
</section>

</body>
</html>
```